Road Construction Company needs business cards

We would like a new business card designed for our business.

We're a road construction company based in Qld, Australia.

Can the business card please have the following information on it.

Name: Brent Malvoy
Position: General Manager
Phone: 0471 592 304
Email: Brent.malvoy@quendix.com.au
Address: 87 Harrowgate Ave, Pindarra, QLD, 4000
Website: www.quendix.com.au

Visually we'd like the card to be professional and simple.

Attached is our logo.

Our website is www.quendix.com.au

Target Market(s)

Men aged 25-60

Contact Information for Business Card

As listed in project description

Font styles to use
Serif

Requirements
Must have
• Large logo on back of card

```html
<!DOCTYPE html>
<html lang="en">
<head>
<meta charset="utf-8">
<title>Quendix Business Card</title>
<link rel="stylesheet" href="https://fonts.googleapis.com/css2?family=Montserrat:wght@400;500;600;800&display=swap">
<style>
  :root {
    --navy: #0d56a6;
    --sky: #2fa3d8;
    --ink: #1f1f22;
    --paper: #ffffff;
    --backdrop: #3c3c3f;
  }
  * { box-sizing: border-box; margin: 0; padding: 0; }
  html, body { width: 1200px; height: 1059px; overflow: hidden; }
  body {
    background: var(--backdrop);
    font-family: "Montserrat", Arial, sans-serif;
    position: relative;
  }
  .card {
    position: absolute;
    border-radius: 24px;
    overflow: hidden;
  }
  .card-front {
    left: 256px; top: 100px; width: 687px; height: 391px;
    background: var(--paper);
  }
  .card-back {
    left: 253px; top: 537px; width: 694px; height: 395px;
    background: var(--navy);
  }
  .brand-name {
    font-weight: 800;
    letter-spacing: 1px;
    line-height: 1;
    white-space: nowrap;
  }
  .card-front .brand-name {
    position: absolute; right: 29px; top: 52px;
    font-size: 50px; color: var(--navy);
  }
  .card-back .brand-name {
    position: absolute; left: 0; right: 0; top: 160px;
    text-align: center;
    font-size: 72px; color: var(--paper);
  }
  .name-marker {
    position: absolute; left: 0; top: 212px;
    width: 14px; height: 43px; background: var(--navy);
  }
  .person-name {
    position: absolute; left: 30px; top: 206px;
    font-size: 29px; font-weight: 600; color: var(--navy);
    white-space: nowrap;
  }
  .person-name .surname { color: var(--sky); }
  .person-role {
    position: absolute; left: 30px; top: 239px;
    font-size: 17px; font-weight: 400; color: var(--ink);
  }
  .role-rule {
    position: absolute; left: 189px; right: 29px; top: 251px;
    height: 1px; background: var(--sky);
  }
  .contact-list {
    position: absolute; left: 29px; top: 280px;
    list-style: none;
  }
  .contact-list li {
    display: flex; align-items: center;
    height: 26.5px;
    font-size: 16.5px; color: var(--ink);
  }
  .contact-list svg { width: 13px; height: 13px; margin-right: 8px; fill: var(--navy); }
  .address {
    position: absolute; right: 29px; top: 311px;
    text-align: right; font-size: 16.5px; line-height: 20px; color: var(--ink);
    font-style: normal;
  }
  .bottom-band { position: absolute; left: 0; bottom: 0; width: 687px; height: 15px; }
</style>
</head>
<body>
  <section class="card card-front">
    <div class="brand-name">QUENDIX</div>

    <span class="name-marker"></span>
    <h1 class="person-name">Brent <span class="surname">Malvoy</span></h1>
    <p class="person-role">General Manager</p>
    <span class="role-rule"></span>

    <ul class="contact-list">
      <li>
        <svg viewBox="0 0 16 16"><path d="M3.6 1.2l2.3 2.8-1.3 1.7c.9 2 2.6 3.7 4.6 4.6l1.7-1.3 2.8 2.3-1.3 2.4C7.200 14.900 1.100 8.800 1.200 3.600z"/></svg>
        0471 592 304
      </li>
      <li>
        <svg viewBox="0 0 16 16"><path d="M1 3h14v1.2L8 9 1 4.2z"/><path d="M1 5.8L8 10.6l7-4.8V13H1z"/></svg>
        Brent.malvoy@quendix.com.au
      </li>
      <li>
        <svg viewBox="0 0 16 16"><path d="M8 1a7 7 0 100 14A7 7 0 008 1zm0 1.3c.8 0 1.700 1.500 2 3.700H6c.3-2.200 1.200-3.700 2-3.700zM2.400 7.300h2.300a14 14 0 000 1.400H2.400a5.700 5.700 0 010-1.400zm3.500 0h4.200a13 13 0 010 1.400H5.900a13 13 0 010-1.400zm5.400 0h2.300a5.700 5.700 0 010 1.400h-2.300a14 14 0 000-1.400zM6 10h4c-.3 2.200-1.200 3.700-2 3.700S6.300 12.200 6 10z"/></svg>
        www.quendix.com.au
      </li>
    </ul>

    <address class="address">87 Harrowgate Ave,<br>Pindarra, QLD, 4000</address>

    <svg class="bottom-band" viewBox="0 0 687 15" preserveAspectRatio="none">
      <polygon points="0,0 349,0 334,15 0,15" fill="var(--navy)"/>
      <polygon points="355,0 687,0 687,15 340,15" fill="var(--sky)"/>
    </svg>
  </section>

  <section class="card card-back">
    <div class="brand-name">QUENDIX</div>
  </section>
</body>
</html>
```